Rug Cleaning Web Design Project

We need a web design for our cleaning company. We currently have a web page but are not happy with its design. We currently offer fine rug cleaning,upholstery cleaning, and residential and commercial carpet cleanning. We also offer water damage restoration. For our rug cleaning services we offer : Enzyme treatments for pet contamination and odor removal, application of stain protection that is designed for the fine textiles used in rug construction, application of treatments designed to prevent moth damage and pads designed to be used under rugs.Our current web site is harborfreshcare.example. We are intrested in a design with similar information to the web page of Velmora Rug Cleaners INC. We would like to use the colors that are present in our logo that will be uploaded with this description. We would also like this new page to be linked to our other address loomrinsepro.example. We would like the deign to be visually attractive but not "too busy".
Updates

Please include pictures of rugs, or people washing rugs if possible. We do not offer maid type cleaning services. We would not be interested in designs including pictures depicting that type service. Thanks for your hard work on this project.

Dana Whitlow

Industry/Entity Type

Residential

Requirements
Must have
• This page must be viewable on smart phones and tablets.

```html
<!DOCTYPE html>
<html lang="en">
<head>
<meta charset="utf-8">
<title>LoomRinsePro — Harbor Fresh Care, LLC</title>
<link rel="stylesheet" href="https://fonts.googleapis.com/css2?family=Arimo:wght@400;700&family=Open+Sans:wght@300;400&display=swap">
<style>
:root{
  --blue:#1d6fb4;
  --blue-dark:#0d5aa0;
  --blue-light:#3f86c4;
  --ink:#111;
  --text:#555;
  --lead:#4a7fb0;
  --red:#e8321c;
  --footer:#454545;
  --rule:#e2e2e2;
}
*{box-sizing:border-box;margin:0;padding:0}
html,body{width:980px;height:1200px;overflow:hidden;background:#fff}
body{font-family:Arimo,Arial,sans-serif;color:var(--text)}
.page{position:relative;width:980px;height:1200px}

.brand{position:absolute;left:78px;top:26px;display:flex;align-items:center;gap:14px}
.brand-mark{width:58px;height:58px;border-radius:50%;background:var(--blue)}
.brand-name{font-size:40px;font-weight:700;color:#1e1e1e;letter-spacing:-1px;line-height:1}
.brand-sub{font-size:13px;color:#1e1e1e;letter-spacing:4px;margin-top:6px}

.contact{position:absolute;right:80px;top:52px;text-align:right;color:var(--ink)}
.contact-address{font-size:14px}
.contact-phone{font-size:29px;font-weight:700;color:#222;display:flex;align-items:center;justify-content:flex-end;gap:8px;margin-top:2px}

.nav{position:absolute;left:20px;top:130px;width:940px;height:63px;
  background:linear-gradient(#0c5fa7 0,#1a6fb6 50%,#3d83c2 50%,#4d8fca 100%);display:flex;padding-left:104px}
.nav a{display:flex;align-items:center;padding:0 19px;color:#fff;text-decoration:none;font-size:13px;font-weight:700;
  text-shadow:0 1px 1px rgba(0,0,0,.5);border-left:1px solid rgba(255,255,255,.35)}
.nav a:last-child{border-right:1px solid rgba(255,255,255,.35)}

.hero{position:absolute;left:20px;top:203px;width:940px;height:365px;
  background:linear-gradient(165deg,#8b9ed6 0,#7486c4 32%,#5e6aa0 44%,#e23a22 52%,#f0361c 75%,#d82c14 100%);
  box-shadow:0 14px 14px -8px rgba(0,0,0,.45)}
.hero-title{position:absolute;left:60px;top:178px;font-size:55px;font-weight:700;color:#fff;text-shadow:0 2px 4px rgba(0,0,0,.55)}
.hero-caption{position:absolute;left:60px;top:255px;width:680px;height:86px;background:rgba(110,10,5,.6);
  padding:12px 20px;color:#fff;font-size:24px;font-weight:700;line-height:33px}

.col{position:absolute;top:609px;width:300px}
.col-1{left:20px}.col-2{left:340px}.col-3{left:660px}
.col-head{height:48px;background:linear-gradient(#0c5fa7 0,#1a6fb6 50%,#3d83c2 50%,#4d8fca 100%);
  color:#fff;font-family:"Open Sans",Arial,sans-serif;font-size:21px;font-weight:400;padding:11px 23px;text-shadow:0 1px 2px rgba(0,0,0,.5)}

.item{display:flex;gap:16px;height:110px;padding-top:19px;border-bottom:1px solid var(--rule)}
.item:first-of-type{padding-top:19px}
.item:last-of-type{border-bottom:none}
.thumb{width:110px;height:100px;border:1px solid var(--rule);padding:9px;flex:none}
.thumb span{display:block;width:100%;height:100%}
.item-title{font-family:"Open Sans",Arial,sans-serif;font-size:16px;color:var(--blue-dark);line-height:21px;margin-top:4px}
.item-text{font-size:12px;line-height:17px;margin-top:6px}

.lead{font-family:"Open Sans",Arial,sans-serif;font-size:15px;line-height:22px;color:var(--lead);margin-top:26px}
.body{font-size:12px;line-height:18px;margin-top:17px}

.photo{width:300px;height:160px;border:1px solid var(--rule);padding:9px;margin-top:27px}
.photo span{display:block;width:100%;height:100%;background:linear-gradient(90deg,#3d4a60 0,#5a6274 15%,#e8781c 22%,#f08a24 60%,#e5731a 100%)}

.more{position:absolute;top:1025px;width:150px;height:33px;
  background:linear-gradient(#0c5fa7 0,#1a6fb6 50%,#3d83c2 50%,#4d8fca 100%);
  color:#fff;font-size:19px;font-weight:700;padding:5px 23px;text-shadow:0 1px 2px rgba(0,0,0,.5);text-decoration:none}

.footer{position:absolute;left:20px;top:1086px;width:940px;height:95px;background:var(--footer);
  color:#fff;text-align:center;font-size:12.5px;line-height:17px;padding-top:25px}
</style>
</head>
<body>
<div class="page">
  <header>
    <div class="brand">
      <span class="brand-mark"></span>
      <div>
        <div class="brand-name">LoomRinsePro</div>
        <div class="brand-sub">HARBOR FRESH CARE, LLC</div>
      </div>
    </div>
    <div class="contact">
      <div class="contact-address">48 Fenwick Lane, Ashbury, AL&nbsp; 35000</div>
      <div class="contact-phone">
        <svg width="24" height="24" viewBox="0 0 24 24" aria-hidden="true"><path fill="#333" d="M6.6 2.5l3 3.6-2 2.4c1 2.6 3.3 5 5.9 6l2.4-2 3.6 3-2.2 3.2C10.6 19 5 13.4 3.4 5.7z"/></svg>
        (256) 555-0142
      </div>
    </div>
  </header>

  <nav class="nav">
    <a href="#">HOME</a><a href="#">ABOUT US</a><a href="#">RUG WASHING</a><a href="#">WATER DAMAGE</a><a href="#">CARPET CLEANING</a><a href="#">CONTACT</a>
  </nav>

  <section class="hero" role="img" aria-label="Close-up of blue and red shaggy rug fibres">
    <h1 class="hero-title">Velit Denique</h1>
    <p class="hero-caption">Eu saperet consequat dissentiunt duo, ei duo feugiat offendit. Et sit verear consetetur inciderint, labore</p>
  </section>

  <section class="col col-1">
    <h2 class="col-head">VIDE IMPERDIET</h2>
    <div class="item">
      <div class="thumb"><span role="img" aria-label="Red shag rug close-up" style="background:linear-gradient(135deg,#f03a1e,#c8200e)"></span></div>
      <div><h3 class="item-title">VIDE IMPERDIET LABORIS</h3><p class="item-text">Lorem ipsum dolor sit amet, eam nusquam similique</p></div>
    </div>
    <div class="item">
      <div class="thumb"><span role="img" aria-label="Vacuum nozzle on a green carpet" style="background:linear-gradient(90deg,#c6cf3a,#d9e05a)"></span></div>
      <div><h3 class="item-title">VIDE IMPERDIET LABORIS</h3><p class="item-text">Lorem ipsum dolor sit amet, eam nusquam similique</p></div>
    </div>
    <div class="item">
      <div class="thumb"><span role="img" aria-label="Brush cleaning a colourful rug" style="background:linear-gradient(135deg,#4c7fd0,#9a6ab8 60%,#c06a9a)"></span></div>
      <div><h3 class="item-title">VIDE IMPERDIET LABORIS</h3><p class="item-text">Lorem ipsum dolor sit amet, eam nusquam similique</p></div>
    </div>
  </section>

  <section class="col col-2">
    <h2 class="col-head">VIDE IMPERDIET</h2>
    <p class="lead">Lorem ipsum dolor sit amet, eam nusquam similique sadipscing eu, ius mutat periculis disputationi ea, id cum</p>
    <p class="body">Lorem ipsum dolor sit amet, eam nusquam similique sadipscing eu, ius mutat periculis disputationi ea, id cum sale persecuti. Vide imperdiet ea mei, sed dictas appetere oporteat ne. Ignota inimicus recteque est te, paulo graeci</p>
    <p class="body">Lorem ipsum dolor sit amet, eam nusquam similique sadipscing eu, ius mutat periculis disputationi ea, id cum sale persecuti. Vide imperdiet ea mei, sed dictas appetere oporteat ne. Ignota inimicus recteque est te, paulo graeci ornatus sit ea. Usu dicta senserit dissentiunt eu, graecis incorrupte usu id, ei laoreet principes nam.</p>
  </section>

  <section class="col col-3">
    <h2 class="col-head">VIDE IMPERDIET</h2>
    <div class="photo"><span role="img" aria-label="Vacuum cleaner head on an orange carpet"></span></div>
    <p class="body" style="margin-top:25px">Lorem ipsum dolor sit amet, eam nusquam similique sadipscing eu, ius mutat periculis disputationi ea, id cum sale persecuti. Vide imperdiet ea mei, sed dictas appetere oporteat ne. Ignota inimicus recteque est te, paulo graeci ornatus sit ea. Usu dicta senserit dissentiunt eu, graecis incorrupte usu id, ei laoreet principes nam.</p>
  </section>

  <a class="more" href="#" style="left:20px">Read more</a>
  <a class="more" href="#" style="left:340px">Read more</a>
  <a class="more" href="#" style="left:660px">Read more</a>

  <footer class="footer">
    <p>Copyright © 2012 Harbor Fresh Care, LLC</p>
    <p>Nec et erant clita consul, ius eu mazim nullam euripidis, his velit percipit et. Eam mundi</p>
    <p>Nec et erant clita consul, ius eu mazim nullam euripidis, his</p>
  </footer>
</div>
</body>
</html>
```